Holvern Incorporated

Holvern is a business that provides consulting, and manages and supplies trades persons in the construction and heavy industries sector. We build, do maintenance, install machinery, and can manage projects or jobs. Would like or prefer more clean, classic designs. Blacks/greys, but open to almost anything.

Target Market(s)

Industrial/Construction/Manufacturing

Industry/Entity Type

Construction Company

Contact Information for Business Card

Clean, business name on the front, possibly have the details on the back, but open to any ideas.

Logo Text

We currently do not have a slogan, open to ideas

Font styles to use
Serif
Sans Serif

Colors

Designer to choose colors to be used in the design.

Requirements
Should not have
• the oval is not my logo, was just an idea. please don't send 20 designs with the oval

```html
<!DOCTYPE html>
<html lang="en">
<head>
<meta charset="utf-8">
<title>Holvern Incorporated — Business Card</title>
<link href="https://fonts.googleapis.com/css2?family=Work+Sans:wght@400;500&display=swap" rel="stylesheet">
<style>
  :root {
    --backdrop: #151515;
    --card: #232323;
    --card-edge: #2c2c2c;
    --silver: #c9c9c9;
    --silver-soft: #a9a9a9;
    --rule: #8a8a8a;
  }
  * { box-sizing: border-box; margin: 0; padding: 0; }
  html, body {
    width: 1200px;
    height: 900px;
    overflow: hidden;
    background: var(--backdrop);
  }
  .canvas {
    width: 1200px;
    height: 900px;
    display: flex;
    flex-direction: column;
    align-items: center;
    justify-content: center;
    gap: 36px;
  }
  .card {
    width: 700px;
    height: 400px;
    background: var(--card);
    border: 1px solid var(--card-edge);
    position: relative;
    font-family: "Work Sans", sans-serif;
    color: var(--silver);
  }
  .card-front {
    display: flex;
    align-items: center;
    justify-content: center;
  }
  .wordmark {
    display: flex;
    align-items: center;
    gap: 14px;
    font-family: "Work Sans", sans-serif;
    font-weight: 500;
    color: var(--silver);
    letter-spacing: 0.04em;
  }
  .wordmark-dot {
    width: 14px;
    height: 14px;
    border-radius: 50%;
    background: var(--silver);
  }
  .card-front .wordmark { font-size: 34px; }
  .card-back {
    display: flex;
    align-items: center;
  }
  .card-back .brand-side {
    width: 330px;
    display: flex;
    justify-content: center;
  }
  .card-back .wordmark { font-size: 24px; }
  .divider {
    width: 1px;
    height: 200px;
    background: var(--rule);
  }
  .details {
    padding-left: 36px;
    font-size: 18px;
    line-height: 1.45;
    color: var(--silver-soft);
  }
  .person-name {
    font-size: 26px;
    font-weight: 500;
    letter-spacing: 0.06em;
    color: var(--silver);
    text-transform: uppercase;
  }
  .person-role {
    font-size: 17px;
    margin-bottom: 14px;
  }
  .address { margin-bottom: 6px; }
  .contact-line {
    display: flex;
    align-items: center;
    gap: 10px;
  }
  .contact-line svg {
    width: 13px;
    height: 13px;
    flex: none;
    stroke: var(--silver-soft);
    fill: none;
    stroke-width: 1.6;
  }
</style>
</head>
<body>
<main class="canvas">
  <section class="card card-front">
    <div class="wordmark"><span class="wordmark-dot"></span>Holvern Incorporated</div>
  </section>

  <section class="card card-back">
    <div class="brand-side">
      <div class="wordmark"><span class="wordmark-dot"></span>Holvern Incorporated</div>
    </div>
    <div class="divider"></div>
    <div class="details">
      <div class="person-name">Daniel Rourke</div>
      <div class="person-role">Director</div>
      <div class="address">1480 Ashcombe<br>Road Cedar Falls, FL 32190</div>
      <div class="contact-line">
        <svg viewBox="0 0 16 16"><path d="M4 1.5 L6.5 5 L5 6.5 Q6.5 9.5 9.5 11 L11 9.5 L14.5 12 L13 14.5 Q6 14 1.5 3 Z"/></svg>
        555.214.6730
      </div>
      <div class="contact-line">
        <svg viewBox="0 0 16 16"><rect x="1.5" y="3.5" width="13" height="9"/><path d="M1.5 3.5 L8 9 L14.5 3.5"/></svg>
        info@holvernworks.ca
      </div>
      <div class="contact-line">
        <svg viewBox="0 0 16 16"><circle cx="8" cy="8" r="6.5"/><path d="M1.5 8 H14.5 M8 1.5 Q4.5 8 8 14.5 M8 1.5 Q11.5 8 8 14.5"/></svg>
        www.holvernworks.ca
      </div>
    </div>
  </section>
</main>
</body>
</html>
```